French Puns

Creation of a cover for a book on French plays on words.
The public is lovers of the French language
TITLE: The gentle phrases of Honoré Vasseline
SUB-TITLE: Witty words, wit of words
PUBLISHER (at the bottom of the page): Editions Plumeau
(See joined examples, previous books of the same author)
Size: 14 x 20.5 cm
Please note that the text on the cover is in French, not in English:
Fine phrases from Honoré Vasseline
Witty words, witty words (subtitle, smaller)
Plumeau Editions

```html
<!DOCTYPE html>
<html lang="fr">
<head>
<meta charset="utf-8">
<title>Les bons mots d'Honoré Vasseline</title>
<link rel="stylesheet" href="https://fonts.googleapis.com/css2?family=Spirax&family=Open+Sans:wght@400;500&display=swap">
<style>
  :root {
    --paper: #d9c29c;
    --paper-light: #e8d8ba;
    --paper-dark: #bfa47c;
    --ink: #1f150c;
    --gold: #b8832a;
    --subtitle: #3f3510;
    --publisher: #2a2418;
    --jester-red: #d2643c;
    --jester-teal: #4f9a86;
    --jester-cream: #e9ddc6;
  }
  html, body {
    margin: 0;
    padding: 0;
    width: 820px;
    height: 1200px;
    overflow: hidden;
    background: var(--paper);
  }
  .cover {
    position: relative;
    width: 820px;
    height: 1200px;
    overflow: hidden;
    background:
      radial-gradient(ellipse at 50% 55%, var(--paper-light) 0%, var(--paper) 55%, var(--paper-dark) 100%);
  }
  .cover-title {
    position: absolute;
    left: 0;
    top: 0;
    width: 820px;
    height: 300px;
  }
  .cover-title text {
    font-family: "Spirax", cursive;
    fill: var(--ink);
    stroke: var(--gold);
    stroke-width: 1.2px;
    paint-order: stroke;
  }
  .cover-title .title-shadow {
    fill: rgba(60, 45, 25, 0.35);
    stroke: none;
  }
  .cover-illustration {
    position: absolute;
    left: 110px;
    top: 375px;
    width: 600px;
    height: 640px;
    border-radius: 46% 46% 40% 40%;
    background:
      radial-gradient(ellipse at 50% 22%, var(--jester-red) 0%, rgba(210,100,60,0.55) 28%, transparent 48%),
      radial-gradient(ellipse at 50% 62%, var(--jester-teal) 0%, rgba(79,154,134,0.5) 32%, transparent 60%),
      radial-gradient(ellipse at 50% 90%, rgba(210,100,60,0.7) 0%, transparent 55%),
      radial-gradient(ellipse at 50% 50%, var(--jester-cream) 0%, transparent 70%);
    opacity: 0.9;
  }
  .cover-subtitle {
    position: absolute;
    left: 0;
    width: 820px;
    top: 1050px;
    margin: 0;
    text-align: center;
    font-family: "Spirax", cursive;
    font-weight: 400;
    font-size: 50px;
    color: var(--subtitle);
    letter-spacing: 0.5px;
  }
  .cover-publisher {
    position: absolute;
    right: 104px;
    top: 1114px;
    margin: 0;
    font-family: "Open Sans", sans-serif;
    font-weight: 500;
    font-size: 22px;
    color: var(--publisher);
  }
</style>
</head>
<body>
  <main class="cover">
    <svg class="cover-title" viewBox="0 0 820 300" aria-label="Les bons mots d'Honoré Vasseline">
      <defs>
        <path id="title-arc" d="M 120 165 Q 400 10 680 150"/>
      </defs>
      <text class="title-shadow" font-size="82" transform="translate(5 5)">
        <textPath href="#title-arc" startOffset="50%" text-anchor="middle">Les bons mots</textPath>
      </text>
      <text font-size="82">
        <textPath href="#title-arc" startOffset="50%" text-anchor="middle">Les bons mots</textPath>
      </text>
      <text class="title-shadow" x="415" y="273" font-size="96" text-anchor="middle" textLength="735" lengthAdjust="spacingAndGlyphs">d'Honoré Vasseline</text>
      <text x="410" y="268" font-size="96" text-anchor="middle" textLength="735" lengthAdjust="spacingAndGlyphs">d'Honoré Vasseline</text>
    </svg>

    <div class="cover-illustration" role="img" aria-label="Illustration d'un bouffon en costume rouge et vert, assis en tailleur, lisant un livre, entouré de plumes qui volent"></div>

    <p class="cover-subtitle">Mots d'esprit, esprit des mots</p>
    <p class="cover-publisher">Éditions Plumeau</p>
  </main>
</body>
</html>
```